Real Estate Company Website

We are working with TZ Real Estate and building a new website for them.
Some sites to use for content/competitors and inspiration:
https://lucettabrom.zp.com
https://www.hovelnest.com
https://www.keystrand88.com
https://tobinahaldreth.com
https://pollyvestrum.com
https://oswinbrakel.com
https://marcotuzzlegroup.com
Thank you for taking the time to consider designing a website for us. We are web developers based in Stockton, CA, USA. Most of our projects go through the same process. Understanding this process may help you win a project with us. We custom-code all of our websites in-house. We don’t have any requirements as to what tools you use for your design, but we prefer Figma files. For any design that we label as four stars, we send it to the client for review. The client picks the final design they want us to use. Once we complete this process, we will continue to show additional clients all the four-star sites and purchase them later. Your designs will have multiple chances to sell. For better chances of success, we ask that you follow these guidelines.
IMAGES:
If you use any images or icons in the design, we ask that you have a link to the asset so we can purchase the image/icon. Most of the designs we submit do not have the customer’s images on them unless they have some great images. Be creative; show us the feeling you are trying to portray with your image choices. Use any royalty-free site you choose. We subscribe to Plenvo and mainly use their images, but we can purchase images outside of Plenvo. PLEASE NOTE: we will not submit designs to clients with watermarks on the images.
FONTS:
We ask that you identify the fonts used in the design. This can be done in a message if you want. We typically use Google Fonts and Plenvo Fonts.
CONTENT:
We're always open to different content and ideas. We often submit designs with stock images so the client can see our vision. We typically take pictures after the website launch to use their images with our vision. Lorem Ipsum is fine for paragraphs, but we ask that you write the headers in correct English. We want to be able to show the vision and identify the sections of the website.
INSPIRATION:
We typically add a couple of links in the brief of websites we like to help you get started in your design.
REVISIONS:
We do not often ask for revisions of the designs unless we see something in the design that may not appeal to the client. If there are slight changes that we want to make, we do that in the development process.
FEEDBACK:
We rarely give feedback on designs during the design process. We are working on many website projects and do not have the time to provide feedback. We usually respond if your request is well thought out and asks specific questions, but a note asking “feedback, please” usually goes unanswered.

```html
<!DOCTYPE html>
<html lang="en">
<head>
<meta charset="utf-8">
<title>TZ Real Estate</title>
<link href="https://fonts.googleapis.com/css2?family=Cinzel:wght@500;600&family=Roboto:wght@400;500&display=swap" rel="stylesheet">
<style>
:root{
  --teal:#17687a;
  --teal-dark:#115463;
  --ink:#1a1a1a;
  --text:#333;
  --muted:#555;
  --soft:#f4f4f4;
  --white:#fff;
  --footer:#0b0b0b;
  --star:#f5a623;
}
*{box-sizing:border-box;margin:0;padding:0}
html,body{width:1200px;height:4563px;overflow:hidden}
body{position:relative;font-family:"Roboto",sans-serif;color:var(--text);background:var(--white)}
.abs{position:absolute}
.serif{font-family:"Cinzel",serif;font-weight:500;color:var(--ink);letter-spacing:1px}
.kicker{color:var(--teal);font-weight:400}
.btn{position:absolute;display:flex;align-items:center;justify-content:center;border-radius:30px;font-size:16px;text-transform:uppercase;font-weight:400}
.btn-outline{border:2px solid var(--teal);color:var(--teal);background:var(--white)}
.btn-solid{background:var(--teal);color:var(--white)}
.photo{position:absolute}

/* header */
.site-header{position:absolute;left:0;top:0;width:1200px;height:115px;background:linear-gradient(90deg,#4d5761,#66707a 60%,#6f7881);z-index:2}
.brand{position:absolute;left:72px;top:30px;color:var(--white);font-family:"Cinzel",serif;font-size:24px;font-weight:600;line-height:1.1;display:flex;align-items:center;gap:10px}
.brand-mark{width:14px;height:14px;background:var(--white)}
.nav{position:absolute;top:48px;left:538px;display:flex;gap:0;font-size:12px;color:var(--white)}
.nav span{position:absolute;white-space:nowrap}
.nav .active::after{content:"";position:absolute;left:-3px;right:-3px;top:26px;height:2px;background:var(--white)}
.login{position:absolute;left:1021px;top:40px;width:105px;height:34px;background:var(--white);border-radius:20px;color:var(--teal);font-size:13px;display:flex;align-items:center;justify-content:center;gap:7px}

/* hero */
.hero{position:absolute;left:0;top:115px;width:1200px;height:585px;background:linear-gradient(90deg,#c7d6e4 0%,#d6e2ec 35%,#e6edf3 100%)}
.hero-photo{left:460px;top:0;width:740px;height:585px;background:linear-gradient(180deg,#b9cde0 0%,#dfe6ec 45%,#c8a27a 72%,#e9eef2 100%);opacity:.85}
.hero-kicker{left:74px;top:108px;font-size:30px}
.hero-title{left:74px;top:150px;font-size:58px;line-height:64px}
.search-panel{position:absolute;left:128px;top:553px;width:944px;height:209px;background:var(--teal)}
.search-label{position:absolute;left:79px;top:48px;color:var(--white);font-size:19px}
.search-field{position:absolute;left:46px;top:92px;width:852px;height:64px;background:var(--white);border-radius:34px;font-size:12px;color:#666;padding-left:33px;display:flex;align-items:center}
.search-btn{position:absolute;right:4px;top:4px;width:182px;height:56px;background:var(--teal);border-radius:30px;color:var(--white);font-size:19px;display:flex;align-items:center;justify-content:center;gap:12px}

/* about */
.about-frame{left:122px;top:867px;width:369px;height:407px;border:2px solid var(--teal-dark)}
.about-photo{left:142px;top:883px;width:368px;height:411px;background:linear-gradient(160deg,#eceae6 0%,#d9d4cc 55%,#b48a5e 100%)}
.about-kicker{left:588px;top:866px;font-size:39px}
.about-title{left:585px;top:915px;font-size:50px}
.about-copy{left:585px;top:1006px;width:495px;font-size:15px;line-height:30px;color:var(--ink)}

/* services */
.service-photo{top:1398px;width:335px;height:320px}
.service-label{top:1748px;width:335px;text-align:center;font-size:25px;color:var(--ink)}

/* stats */
.stats{position:absolute;left:0;top:1888px;width:1200px;height:283px;background:linear-gradient(90deg,#2b7183,#316f80 50%,#3a7a8a)}
.stat{position:absolute;top:82px;color:var(--white)}
.stat-num{font-size:46px;line-height:1;padding-bottom:14px;border-bottom:3px solid var(--white);display:inline-block;min-width:78px}
.stat-label{font-size:20px;margin-top:18px;white-space:nowrap}

/* featured */
.section-kicker{width:1200px;text-align:center;font-size:42px}
.section-title{width:1200px;text-align:center;font-size:54px}
.filter{top:2449px;height:50px;font-size:19px}
.prop-card{position:absolute;top:2570px;width:314px;height:530px;background:var(--white);box-shadow:0 2px 12px rgba(0,0,0,.15)}
.prop-photo{left:10px;top:10px;width:294px;height:258px}
.prop-tag{position:absolute;left:28px;top:28px;background:#111;color:var(--white);font-size:14px;padding:7px 18px;border-radius:16px}
.prop-price{position:absolute;left:40px;top:296px;font-size:29px;color:var(--teal)}
.prop-name{position:absolute;left:40px;top:344px;font-size:26px;color:var(--ink)}
.prop-meta{position:absolute;left:40px;top:383px;width:250px;font-size:14.5px;line-height:27px;color:var(--ink)}
.prop-buy{left:40px;top:449px;width:132px;height:38px;font-size:16px;text-transform:none}
.stars{position:absolute;left:40px;top:455px;color:var(--star);font-size:21px;letter-spacing:1px}

/* blog */
.blog{position:absolute;left:0;top:3309px;width:1200px;height:867px;background:var(--soft)}
.post{position:absolute;top:261px;width:330px}
.post-shade{position:absolute;left:0;top:0;width:26px;height:230px;background:#3b3b3b}
.post-photo{left:0;top:0;width:296px;height:167px}
.post-title{position:absolute;left:78px;top:199px;width:260px;font-size:19.5px;line-height:24px;color:var(--teal)}
.post-copy{position:absolute;left:78px;top:262px;width:248px;font-size:13.5px;line-height:21px;color:var(--ink)}
.post-link{position:absolute;left:81px;top:358px;font-size:14px;color:var(--teal);text-decoration:underline}

/* footer */
.footer{position:absolute;left:0;top:4176px;width:1200px;height:332px;background:var(--footer);color:var(--white)}
.footer-brand{position:absolute;left:112px;top:106px;font-family:"Cinzel",serif;font-size:30px;font-weight:600;display:flex;align-items:center;gap:12px}
.footer-brand span{width:18px;height:18px;background:var(--teal);display:block}
.social{position:absolute;top:250px;width:28px;height:28px;background:var(--teal)}
.foot-head{position:absolute;top:80px;font-size:20px}
.foot-links{position:absolute;left:413px;top:126px;font-size:14px;line-height:26.6px}
.foot-links li{list-style:none;padding-left:24px;position:relative}
.foot-links li::before{content:"›";position:absolute;left:0;color:var(--teal);font-size:16px}
.contact{position:absolute;left:604px;font-size:13px;line-height:16px;display:flex;gap:22px}
.contact-icon{width:24px;height:24px;background:var(--teal);border-radius:4px;flex:none;display:flex;align-items:center;justify-content:center}
.news-copy{position:absolute;left:869px;top:129px;width:240px;font-size:13px;line-height:18px}
.news-input{position:absolute;left:870px;top:181px;width:218px;height:32px;background:var(--white)}
.news-btn{position:absolute;left:870px;top:233px;width:110px;height:33px;background:var(--teal);border-radius:18px;font-size:11px;font-weight:500;display:flex;align-items:center;justify-content:center}
.copyright{position:absolute;left:0;top:4508px;width:1200px;height:55px;background:var(--teal-dark);color:var(--white);font-size:13px;display:flex;align-items:center;justify-content:center}
</style>
</head>
<body>

<header class="site-header">
  <div class="brand"><span class="brand-mark"></span>TZ Real Estate</div>
  <nav class="nav">
    <span class="active" style="left:0">HOME</span>
    <span style="left:80px">ABOUT US</span>
    <span style="left:185px">PROPERTIES</span>
    <span style="left:302px">BLOG</span>
    <span style="left:376px">CONTACT US</span>
  </nav>
  <div class="login">
    <svg width="13" height="13" viewBox="0 0 14 14"><circle cx="7" cy="4" r="3.2" fill="#17687a"/><path d="M1 14c0-4 3-6 6-6s6 2 6 6z" fill="#17687a"/></svg>Login
  </div>
</header>

<section class="hero">
  <div class="photo hero-photo" role="img" aria-label="Modern white two-storey villa with wooden accents and glass walls"></div>
  <p class="abs kicker hero-kicker">Explore Local Real Estate</p>
  <h1 class="abs serif hero-title">FIND A HOME<br>TO SUIT YOUR<br>LIFESTYLE</h1>
</section>

<div class="search-panel">
  <p class="search-label">FIND HOMES OR AGENTS</p>
  <div class="search-field">City, Neighborhood, Address, Postal Code, School District
    <div class="search-btn">
      <svg width="24" height="24" viewBox="0 0 24 24" fill="none" stroke="#fff" stroke-width="2"><circle cx="10" cy="10" r="7"/><path d="M15 15l6 6"/></svg>Search
    </div>
  </div>
</div>

<section class="about">
  <div class="abs about-frame"></div>
  <div class="photo about-photo" role="img" aria-label="Bright kitchen with dining table, chairs and wicker pendant lamps"></div>
  <p class="abs kicker about-kicker">About</p>
  <h2 class="abs serif about-title">TZ REAL ESTATE</h2>
  <p class="abs about-copy">Lorem ipsum dolor sit amet, consectetur adipiscing elit, sed do eius mod tempor incididunt ut labore et dolore magna aliqua. Ut enim ad minim veniam, quis nostrud exercitation ullamco laboris nisi ut aliquip ex ea commodo consequat. Lorem ipsum dolor sit amet, con sectetur adipiscing elit, sed do eius mod tempor incididunt ut labore et dolore magna aliqua. Ut enim ad minim veniam,.</p>
  <div class="btn btn-outline" style="left:585px;top:1219px;width:177px;height:59px">Learn More</div>
  <div class="btn btn-solid" style="left:776px;top:1219px;width:201px;height:59px">Success Stories</div>
</section>

<section class="services">
  <div class="photo service-photo" style="left:76px;background:linear-gradient(180deg,#c9d6e2,#9aa4a8 50%,#4e5a4e)" role="img" aria-label="Modern apartment building with glass balconies"></div>
  <div class="photo service-photo" style="left:434px;background:linear-gradient(180deg,#a9c7e2,#eef0ef 55%,#b78456)" role="img" aria-label="Modern villa with wooden terrace"></div>
  <div class="photo service-photo" style="left:789px;background:linear-gradient(180deg,#3f7fc4,#8fb4d8 50%,#5d7893)" role="img" aria-label="Glass office towers under blue sky"></div>
  <p class="abs service-label" style="left:76px">Exclusive Listings</p>
  <p class="abs service-label" style="left:434px">Your Home’s Worth</p>
  <p class="abs service-label" style="left:789px">Market Trends</p>
</section>

<section class="stats" role="img" aria-label="Teal tinted interior backdrop with key figures">
  <div class="stat" style="left:112px"><div class="stat-num">650</div><p class="stat-label">Homes For Sale</p></div>
  <div class="stat" style="left:379px"><div class="stat-num">30</div><p class="stat-label">New Listings</p></div>
  <div class="stat" style="left:622px"><div class="stat-num">478+</div><p class="stat-label">Real Estate Agents</p></div>
  <div class="stat" style="left:911px"><div class="stat-num">15</div><p class="stat-label">Real Estate Offices</p></div>
</section>

<section class="featured">
  <p class="abs kicker section-kicker" style="left:0;top:2281px">TZ Real Estates</p>
  <h2 class="abs serif section-title" style="left:0;top:2333px">FEATURED PROPERTIES</h2>
  <div class="btn btn-solid filter" style="left:372px;width:146px">All</div>
  <div class="btn btn-outline filter" style="left:528px;width:146px;border-color:#222;color:#222">Buying</div>
  <div class="btn btn-outline filter" style="left:682px;width:146px;border-color:#222;color:#222">For Sale</div>

  <article class="prop-card" style="left:115px">
    <div class="photo prop-photo" style="background:linear-gradient(180deg,#b9cde0,#e5e5e2 45%,#b4804f 75%,#6e7a5c)" role="img" aria-label="Two-storey family house with garage"></div>
    <p class="prop-price">$7,495,000</p>
    <h3 class="prop-name">Best Property One</h3>
    <p class="prop-meta">6 beds • 4 baths • 1 half baths •<br>6,030 sqft</p>
    <div class="btn btn-solid prop-buy">Buy Now</div>
  </article>
  <article class="prop-card" style="left:443px">
    <div class="photo prop-photo" style="background:linear-gradient(180deg,#b8c3c5,#8f7760 50%,#5b5a4e)" role="img" aria-label="Aerial view of a modern house with courtyard"></div>
    <span class="prop-tag">FOR SALE</span>
    <p class="prop-price">$1,275,000</p>
    <h3 class="prop-name">Best Property Two</h3>
    <p class="prop-meta">6 beds • 4 baths • 1 half baths •<br>6,030 sqft</p>
    <p class="stars">★★★★★</p>
  </article>
  <article class="prop-card" style="left:771px">
    <div class="photo prop-photo" style="background:linear-gradient(90deg,#f2f2f2 40%,#b36a3e 60%,#8a4f2e)" role="img" aria-label="House facade with white walls and wooden cladding"></div>
    <p class="prop-price">$2,500,000</p>
    <h3 class="prop-name">Best Property Three</h3>
    <p class="prop-meta">6 beds • 4 baths • 1 half baths •<br>6,030 sqft</p>
    <div class="btn btn-solid prop-buy">Buy Now</div>
  </article>

  <div class="btn btn-outline" style="left:510px;top:3155px;width:180px;height:58px">View More</div>
</section>

<section class="blog">
  <p class="abs kicker section-kicker" style="left:0;top:87px">Blog</p>
  <h2 class="abs serif section-title" style="left:0;top:140px">LATEST NEWS &amp; UPDATES</h2>

  <article class="post" style="left:71px">
    <div class="post-shade"></div>
    <div class="photo post-photo" style="background:linear-gradient(180deg,#4e6f94,#eef1f4 55%,#6b6b5e)" role="img" aria-label="White house with blue roof among trees"></div>
    <h3 class="post-title">Lorem ipsum dolor sit amet, consectetur adipiscing</h3>
    <p class="post-copy">Lorem ipsum dolor sit amet, consecte tur adipiscing elit. Sed eget eros et dui consectetur molestie. Nulla pharetra varius ullamcorper.</p>
    <p class="post-link">READ MORE</p>
  </article>
  <article class="post" style="left:443px">
    <div class="post-shade"></div>
    <div class="photo post-photo" style="background:linear-gradient(180deg,#6d625a,#c8bcb0 50%,#4a3f38)" role="img" aria-label="Living room with dark shelving and armchairs"></div>
    <h3 class="post-title">Lorem ipsum dolor sit amet, consectetur adipiscing</h3>
    <p class="post-copy">Lorem ipsum dolor sit amet, consecte tur adipiscing elit. Sed eget eros et dui consectetur molestie. Nulla pharetra varius ullamcorper.</p>
    <p class="post-link">READ MORE</p>
  </article>
  <article class="post" style="left:814px">
    <div class="post-shade"></div>
    <div class="photo post-photo" style="background:linear-gradient(180deg,#e4d6c8,#b99886 55%,#7b6a63)" role="img" aria-label="Warm lit lounge with sofa and shelves"></div>
    <h3 class="post-title">Lorem ipsum dolor sit amet, consectetur adipiscing</h3>
    <p class="post-copy">Lorem ipsum dolor sit amet, consecte tur adipiscing elit. Sed eget eros et dui consectetur molestie. Nulla pharetra varius ullamcorper.</p>
    <p class="post-link">READ MORE</p>
  </article>

  <div class="btn btn-outline" style="left:510px;top:700px;width:180px;height:61px">View More</div>
</section>

<footer class="footer">
  <div class="footer-brand"><span></span>TZ Real Estate</div>
  <div class="social" style="left:161px"></div>
  <div class="social" style="left:197px"></div>
  <div class="social" style="left:233px"></div>

  <h4 class="foot-head" style="left:413px">Quick Links</h4>
  <ul class="foot-links">
    <li>Home</li><li>About Us</li><li>Properties</li><li>Blog</li><li>Contact Us</li>
  </ul>

  <h4 class="foot-head" style="left:604px">Contact Details</h4>
  <div class="contact" style="top:130px">
    <span class="contact-icon"><svg width="12" height="12" viewBox="0 0 12 12"><path d="M2 1l2 0 1 3-1.5 1a6 6 0 003 3L8 7l3 1v2c0 1-1 1-1 1C5 11 1 7 1 2c0 0 0-1 1-1z" fill="#fff"/></svg></span>
    <p>CALL US<br>8012 345 6789</p>
  </div>
  <div class="contact" style="top:180px">
    <span class="contact-icon"><svg width="12" height="10" viewBox="0 0 12 10"><rect x="0.5" y="0.5" width="11" height="9" fill="#fff"/><path d="M1 1l5 4 5-4" stroke="#17687a" fill="none"/></svg></span>
    <p>EMAIL US<br>info@websitename.com</p>
  </div>
  <div class="contact" style="top:230px">
    <span class="contact-icon"><svg width="10" height="13" viewBox="0 0 10 13"><path d="M5 0a5 5 0 00-5 5c0 4 5 8 5 8s5-4 5-8a5 5 0 00-5-5z" fill="#fff"/><circle cx="5" cy="5" r="1.8" fill="#17687a"/></svg></span>
    <p>Address line here dummy<br>Address line here</p>
  </div>

  <h4 class="foot-head" style="left:869px">Our Newsletter</h4>
  <p class="news-copy">Subscribe our newsletter to get the latest news.</p>
  <div class="news-input"></div>
  <div class="news-btn">SUBSCRIBE</div>
</footer>
<div class="copyright">Copyright ©2023 - All Rights Reserved by Company name</div>

</body>
</html>
```